Coralbend Pastoral Traders Business Cards

We require business cards revamped with our logo. A few details we would like to use.

1. Round Edges
2. Our logo over the top of a wagyu cattle background photo on one side of the card

Other side of the card has the below details.

1. Person Name (First & Last)
2. Job Position
3. Mobile Number
4. Email Address
5. Website Address

Simple & Neat.

Target Market(s)

Sales

Industry/Entity Type

Agriculture

Contact Information for Business Card

CORALBEND PASTORAL TRADERS

Colors

Designer to choose colors to be used in the design.

Requirements
Must have
• Company Logo

```html
<!DOCTYPE html>
<html lang="en">
<head>
<meta charset="utf-8">
<title>Coralbend Pastoral Traders – Business Cards</title>
<link rel="stylesheet" href="https://fonts.googleapis.com/css2?family=Cinzel:wght@600;700&family=Montserrat:wght@400;500&display=swap">
<style>
  :root {
    --page-bg: #2b2d2f;
    --maroon: #640d26;
    --maroon-emboss: #9a2c48;
    --ink: #6b1024;
    --paper: #ffffff;
    --blush: #ecdfe0;
    --text-dark: #3a3a3a;
  }
  * { box-sizing: border-box; margin: 0; padding: 0; }
  html, body { width: 1200px; height: 939px; overflow: hidden; }
  body {
    background: var(--page-bg);
    position: relative;
    font-family: "Montserrat", sans-serif;
  }
  .card {
    position: absolute;
    left: 290px;
    width: 620px;
    height: 354px;
    border-radius: 34px;
    overflow: hidden;
  }
  .card--back { top: 90px; background: var(--maroon); }
  .card--front { top: 495px; background: var(--paper); }

  .wordmark {
    font-family: "Cinzel", serif;
    font-weight: 700;
    text-transform: uppercase;
    line-height: 1.2;
  }
  .card--back .wordmark {
    position: absolute;
    left: 0; right: 0; top: 152px;
    text-align: center;
    font-size: 30px;
    letter-spacing: 2px;
    color: var(--maroon-emboss);
  }
  .card--front .wordmark {
    position: absolute;
    left: 44px; top: 140px;
    width: 220px;
    font-size: 16px;
    letter-spacing: 1px;
    color: var(--ink);
  }

  .cattle-area {
    position: absolute;
    left: 130px; top: 150px;
    width: 280px; height: 204px;
    background: radial-gradient(ellipse 50% 55% at 50% 62%,
      var(--blush) 0%, rgba(236,223,224,0.7) 50%, rgba(236,223,224,0) 100%);
  }

  .person {
    position: absolute;
    left: 300px; top: 58px;
  }
  .person__name {
    font-family: "Cinzel", serif;
    font-weight: 700;
    font-size: 24px;
    letter-spacing: 1px;
    color: var(--ink);
  }
  .person__role {
    font-size: 13px;
    color: var(--text-dark);
    margin-top: 2px;
    margin-left: 14px;
  }

  .contacts {
    position: absolute;
    left: 382px; top: 198px;
    list-style: none;
  }
  .contacts li {
    display: flex;
    align-items: center;
    gap: 7px;
    font-size: 12px;
    color: var(--text-dark);
    margin-bottom: 9px;
  }
  .contacts .phone { letter-spacing: 3px; }
  .contacts svg { width: 12px; height: 12px; fill: var(--ink); flex: none; }
</style>
</head>
<body>

<section class="card card--back" aria-label="Card back">
  <div class="wordmark">Coralbend Pastoral Traders</div>
</section>

<section class="card card--front" aria-label="Card front">
  <div class="cattle-area" role="img" aria-label="Faint silhouette of a standing wagyu cow"></div>

  <div class="wordmark">Coralbend Pastoral Traders</div>

  <div class="person">
    <h1 class="person__name">DECLAN HARWOOD</h1>
    <p class="person__role">Director</p>
  </div>

  <ul class="contacts">
    <li class="phone">
      <svg viewBox="0 0 24 24" aria-hidden="true"><path d="M6.6 10.8a15 15 0 0 0 6.6 6.6l2.2-2.2c.3-.3.7-.4 1-.2 1.1.4 2.3.6 3.6.6.6 0 1 .4 1 1V20c0 .6-.4 1-1 1A17 17 0 0 1 3 4c0-.6.4-1 1-1h3.5c.6 0 1 .4 1 1 0 1.3.2 2.5.6 3.6.1.3 0 .7-.2 1z"/></svg>
      <span>0400-555-127</span>
    </li>
    <li>
      <svg viewBox="0 0 24 24" aria-hidden="true"><path d="M2 5h20v14H2zm2 2v.5l8 5 8-5V7l-8 5z"/></svg>
      <span>info@coralbendpastoral.com.au</span>
    </li>
    <li>
      <svg viewBox="0 0 24 24" aria-hidden="true"><path d="M12 2a10 10 0 1 0 0 20 10 10 0 0 0 0-20zm0 2c1 1.3 1.8 3 2.2 5H9.8c.4-2 1.2-3.7 2.2-5zM9.6 11h4.8a14 14 0 0 1 0 2H9.6a14 14 0 0 1 0-2zm-5.5 0h3.5a16 16 0 0 0 0 2H4.1a8 8 0 0 1 0-2zm12.3 0h3.5a8 8 0 0 1 0 2h-3.5a16 16 0 0 0 0-2zM9.8 15h4.4c-.4 2-1.2 3.7-2.2 5-1-1.3-1.8-3-2.2-5z"/></svg>
      <span>www.coralbendpastoral.com.au</span>
    </li>
  </ul>
</section>

</body>
</html>
```